VELU Natural Hair Care Products

We need a design of label(s) for our natural hair care products for ethnic hair.The products are made of natural ingredients,we would like to see designs that convey a clean and portray a natural feel.
VELU Hair Shampoo - label size 120mm x120mm
VELU Hair Moisturiser - label size 200mm x 25mm
VELU Softener Spray - label size 120mm x120mm

Target Market(s)

Black women with natural hair
High income earners
Natural/Organic market

Industry/Entity Type

Hair

Colors

Designer to choose colors to be used in the design.

Requirements
Must have
• A natural/organic feel or colours

```html
<!DOCTYPE html>
<html lang="en">
<head>
<meta charset="utf-8">
<title>VELU Natural Hair Care Products — Labels</title>
<link rel="stylesheet" href="https://fonts.googleapis.com/css2?family=Oswald:wght@300;500&display=swap">
<style>
  :root {
    --bg: #f5f3f4;
    --ink: #1a1a1a;
    --band: #111111;
    --green: #c6e77f;
    --green-soft: #b6ee8f;
    --mint: #c9eed8;
    --sky: #b9ecf6;
    --cyan: #96e9f6;
  }
  * { margin: 0; padding: 0; box-sizing: border-box; }
  html, body { width: 1200px; height: 1005px; overflow: hidden; background: var(--bg); }
  body { position: relative; font-family: "Oswald", "Arial Narrow", sans-serif; color: var(--ink); }

  .label {
    position: absolute;
    border-top: 8px solid var(--band);
    border-bottom: 8px solid var(--band);
    text-align: center;
    text-transform: uppercase;
  }
  .label--shampoo {
    left: 76px; top: 356px; width: 252px; height: 390px;
    background: linear-gradient(30deg, var(--green) 0%, var(--green) 25%, var(--mint) 60%, var(--sky) 100%);
  }
  .label--spray {
    left: 413px; top: 386px; width: 222px; height: 396px;
    background: linear-gradient(35deg, var(--green-soft) 0%, var(--mint) 45%, var(--cyan) 100%);
  }
  .label--moisturiser {
    left: 733px; top: 700px; width: 390px; height: 162px;
    background: linear-gradient(75deg, var(--green) 0%, var(--mint) 55%, var(--sky) 100%);
  }

  .brand-name {
    display: block;
    font-weight: 300;
    letter-spacing: 0.04em;
    line-height: 1;
    position: absolute; left: 0; right: 0;
  }
  .product-title {
    position: absolute; left: 0; right: 0;
    font-weight: 500; line-height: 1;
  }
  .product-notes {
    position: absolute; left: 0; right: 0;
    font-weight: 500; line-height: 1.6;
  }

  .label--shampoo .brand-name { top: 82px; font-size: 30px; }
  .label--shampoo .product-title { top: 186px; font-size: 19px; }
  .label--shampoo .product-notes { top: 268px; font-size: 13px; }

  .label--spray .brand-name { top: 82px; font-size: 30px; }
  .label--spray .product-title { top: 184px; font-size: 16px; }
  .label--spray .product-notes { top: 272px; font-size: 13.5px; }

  .label--moisturiser .brand-name { top: 18px; font-size: 24px; }
  .label--moisturiser .product-title { top: 60px; font-size: 19px; }
  .label--moisturiser .product-notes { top: 93px; font-size: 10px; line-height: 1.45; }

  .brand-mark {
    position: absolute; left: 770px; top: 270px; width: 320px;
    text-align: center;
    font-weight: 300; font-size: 110px; line-height: 1;
    letter-spacing: 0.04em; color: var(--ink);
  }
</style>
</head>
<body>
  <section class="label label--shampoo" aria-label="VELU Hair Shampoo label">
    <span class="brand-name">VELU</span>
    <h2 class="product-title">2 in 1 Shampoo</h2>
    <p class="product-notes">With olive and peppermint oil<br>Cleansing and conditioning</p>
  </section>

  <section class="label label--spray" aria-label="VELU Softener Spray label">
    <span class="brand-name">VELU</span>
    <h2 class="product-title">Hair Softener Spray</h2>
    <p class="product-notes">With orange oil<br>Daily care and softening</p>
  </section>

  <div class="brand-mark">VELU</div>

  <section class="label label--moisturiser" aria-label="VELU Hair Moisturiser label">
    <span class="brand-name">VELU</span>
    <h2 class="product-title">Hair Moisturizer</h2>
    <p class="product-notes">With cinnamon oil<br>Helps with strengthening and anti-breakage</p>
  </section>
</body>
</html>
```